Dane Morrow films- wedding and event films company website. DESKTOP AND MOBILE

We need a website for a high-end wedding and event film production company. Looking for a very modern and elegant design. my old website is www.danemorrowfilms.example

I like the "white/black/rose gold" color scheme of my logo.

really looking for a sleek modern design the breaths professional and artistic.

Target Market(s)

wedding and event films.

Industry/Entity Type

Film Production

Number of Pages Required

5+ page

Colors

Designer to choose colors to be used in the design.

Requirements
Must have
• website name will be www.danemorrowfilms.example
• tagline is "CINEMATIC STORIES ABOUT YOU"
• sections: HOME, CONTACT, ABOUT, FILMS, BLOG
• You can see my old website at danemorrowfilms.example
• Website about section:
• Dane Morrow Films was Established with the basis of truly cinematic and artistic films in mind. Dane and his team routinely travel the globe documenting weddings and events for high profile clients and discerning couples. Dane was born and raised in Maui Hawaii and has a unique approach to his films that embody the essence of a Hollywood film. Dane has spent the last 10 years traveling the world documenting corporate events and weddings with multiple Award winning production companies. In 2017 Dane decided to establish his own brand “Dane Morrow films” that will take everything he has learned with his past experiences and push it to the next level. Aside from his personal achievements, Dane is extremely passionate about his craft and always looks forward to handcrafting beautiful wedding/event films for his clients. The style of work is non-traditional and the day of filming is extremely unobtrusive (as we are looking for natural-candid/ raw emotions).
• If you are looking for the best price in town, we are probably not the best option, but if you’re looking for the best quality and peace of mind on your wedding day, then you’re in the right place. Dane Morrow Films is a boutique studio that only accepts a limited number of assignments per year. Inquire early to ensure availability.
• LINKS TO VIMEO VIDEOS THAT WILL BE IN THE "FILMS' SECTION.
• BRENT FILM TRAILER - https://clipvault.example/508114362
• BRENT FEATURE FILM - https://clipvault.example/617392048
• JUNE AND ROB'S WEDDING - https://clipvault.example/724958160
• DRONE DEMO REEL - https://clipvault.example/841576203
• WEDDING INDUSTRY EVENT PARTY - https://clipvault.example/962304817/a8d3e7b21c
• images that you can use on site are here: https://brigittolsenimages.proofbox.example/gallery/nora&felix/
• password is: meadow

```html
<!DOCTYPE html>
<html lang="en">
<head>
<meta charset="utf-8">
<title>Dane Morrow Films</title>
<link rel="stylesheet" href="https://fonts.googleapis.com/css2?family=Montserrat:wght@300;400;500;600&family=Cabin:wght@400;500;600&display=swap">
<style>
:root{
  --rose:#c98857;
  --rose-light:#eda263;
  --rose-deep:#b8784a;
  --bar:#c98c58;
  --ink:#2b2b2b;
  --text:#3a3a3a;
  --white:#ffffff;
}
*{box-sizing:border-box;margin:0;padding:0}
html,body{width:1200px;height:2423px;overflow:hidden;background:var(--white)}
body{position:relative;font-family:"Cabin",Arial,sans-serif;color:var(--text)}
.abs{position:absolute}

/* hero */
.hero{left:0;top:0;width:1200px;height:655px;overflow:hidden}
.hero-photo{position:absolute;inset:0;background:
  linear-gradient(180deg,#e9e4dc 0%,#d8cdbd 28%,#9c8f82 45%,#6f655d 62%,#5a5048 100%)}
.hero-photo::after{content:"";position:absolute;inset:0;background:linear-gradient(90deg,rgba(255,255,255,.15),rgba(0,0,0,0) 50%,rgba(255,255,255,.35))}
.hero-wedge{position:absolute;inset:0}
.brand{left:36px;top:120px;font-family:"Montserrat",sans-serif;color:#3d3d3d}
.brand-name{font-size:27px;font-weight:400;letter-spacing:3px}
.brand-sub{font-size:13px;letter-spacing:6px;text-align:center;margin-top:2px;border-top:1px solid #9a7d66;border-bottom:1px solid #9a7d66;width:120px;margin-left:auto;margin-right:auto;line-height:16px}
.brand-dot{position:absolute;left:150px;top:-78px;width:52px;height:52px;background:var(--rose);border-radius:50%}
.nav{right:24px;top:44px;display:flex;gap:28px;font-family:"Montserrat",sans-serif;font-weight:600;font-size:14px;letter-spacing:.5px;color:#222}
.nav a{color:inherit;text-decoration:none;padding-bottom:9px}
.nav a.active{color:var(--rose);border-bottom:3px solid var(--rose)}
.tagline{right:50px;top:516px;text-align:right;color:var(--white);font-family:"Montserrat",sans-serif;font-weight:400}
.tagline-small{font-size:25px;letter-spacing:1.5px}
.tagline-large{font-size:39px;letter-spacing:2px;margin-top:2px}

/* welcome */
.welcome{left:0;top:655px;width:1200px;height:405px;text-align:center}
.section-title{font-family:"Montserrat",sans-serif;font-weight:400;font-size:23px;letter-spacing:1px;color:var(--ink)}
.section-title .accent{color:var(--rose)}
.welcome .section-title{position:absolute;top:106px;left:0;width:1200px}
.welcome-text{position:absolute;left:105px;top:172px;width:990px;font-size:15px;line-height:20px;color:#333}
.btn-more{position:absolute;left:513px;top:300px;width:174px;height:34px;border-radius:4px;background:linear-gradient(180deg,#6c6c6c,#1d1d1d);color:var(--white);font-size:15px;line-height:34px}

/* films */
.films{left:0;top:1060px;width:1200px;height:445px;overflow:hidden;
  background:radial-gradient(ellipse at 50% 78%,#f6c79a 0%,#e9a873 30%,#d89560 60%,#c88a5c 100%)}
.films .section-title{position:absolute;left:0;width:1200px;top:95px;text-align:center;color:var(--white);font-size:20px}
.films-mark{position:absolute;left:584px;top:40px;width:32px;height:32px;border-radius:50%;background:var(--white);opacity:.9}
.video{position:absolute;top:178px;width:330px}
.video-thumb{height:182px;position:relative}
.video-controls{position:absolute;left:10px;right:10px;bottom:8px;height:30px;display:flex;align-items:center;gap:8px}
.ctl-play{width:48px;height:30px;background:rgba(20,20,20,.85);display:flex;align-items:center;justify-content:center}
.ctl-track{flex:1;height:30px;background:rgba(20,20,20,.8);display:flex;align-items:center;padding:0 10px;gap:10px}
.ctl-line{flex:1;height:8px;border:1px solid #888;background:#333}
.ctl-vol{width:26px;height:10px;background:repeating-linear-gradient(90deg,#39a9e6 0 2px,transparent 2px 4px)}
.video-title{margin-top:14px;font-family:"Montserrat",sans-serif;font-size:14px;letter-spacing:1px;color:var(--white)}
.slide-arrow{position:absolute;top:1278px;width:36px;height:70px}

/* blog */
.blog{left:0;top:1505px;width:1200px;height:632px}
.blog .section-title{position:absolute;left:0;width:1200px;top:100px;text-align:center}
.post{position:absolute;overflow:hidden}
.post-caption{position:absolute;left:0;right:0;bottom:0;background:rgba(196,128,76,.82);color:var(--white);padding:12px 24px 14px}
.post-label{font-family:"Montserrat",sans-serif;font-size:14px;letter-spacing:1px;opacity:.95}
.post-text{font-size:14px;font-weight:600;line-height:18px;margin-top:2px}

/* footer */
.footer{left:0;top:2137px;width:1200px;height:258px;background:var(--rose-light);color:var(--white)}
.footer-brand{position:absolute;left:100px;top:120px;font-family:"Montserrat",sans-serif;font-size:24px;letter-spacing:3px;color:#2a2a2a}
.footer-brand-dot{position:absolute;left:246px;top:22px;width:60px;height:60px;border-radius:50%;background:var(--rose-deep)}
.footer-col{position:absolute;top:42px}
.footer-head{font-size:14px;font-weight:600;letter-spacing:.5px;color:#2a2a2a;padding-bottom:10px;border-bottom:1px solid rgba(0,0,0,.2)}
.footer-links{list-style:none;margin-top:14px;font-size:13px;line-height:19.5px}
.contact-row{display:flex;gap:10px;font-size:13px;line-height:18px;margin-top:14px}
.contact-row svg{flex:none;margin-top:1px}
.newsletter-form{display:flex;margin-top:26px}
.newsletter-input{width:170px;height:36px;background:var(--white);border:2px solid #2a2a2a;font-size:13px;font-weight:600;color:#222;padding-left:8px;line-height:32px}
.newsletter-btn{width:93px;height:36px;background:#2a2a2a;color:var(--white);font-size:13px;font-weight:600;text-align:center;line-height:36px;letter-spacing:.5px}
.copyright{left:0;top:2395px;width:1200px;height:28px;background:var(--bar);color:var(--white);text-align:center;font-size:11px;font-weight:600;line-height:28px;letter-spacing:.5px}
</style>
</head>
<body>

<header class="hero abs">
  <div class="hero-photo" role="img" aria-label="Bride and groom embracing on a rocky seaside path at sunset with a lighthouse on the hill"></div>
  <svg class="hero-wedge" width="1200" height="655" viewBox="0 0 1200 655" aria-hidden="true">
    <polygon points="1200,150 680,655 1200,655" fill="#c98a5a" opacity=".9"/>
  </svg>
  <div class="brand abs">
    <span class="brand-dot"></span>
    <div class="brand-name">DANE MORROW</div>
    <div class="brand-sub">FILMS</div>
  </div>
  <nav class="nav abs">
    <a class="active" href="#">HOME</a>
    <a href="#">ABOUT</a>
    <a href="#">FILMS</a>
    <a href="#">BLOG</a>
    <a href="#">CONTACT</a>
  </nav>
  <div class="tagline abs">
    <div class="tagline-small">CINEMATIC STORIES</div>
    <div class="tagline-large">ABOUT YOU</div>
  </div>
</header>

<section class="welcome abs">
  <h2 class="section-title"><span class="accent">WELCOME TO</span> DANE MORROW <span class="accent">FILMS</span></h2>
  <p class="welcome-text">Dane Morrow Films was Established with the basis of truly cinematic and artistic films in mind. Dane and his team routinely travel the globe documenting weddings and events for high profile clients and discerning couples. Dane was born and raised in Maui Hawaii and has a unique approach to his films that embody the essence of a Hollywood film. Dane has spent the last 10 years traveling the world documenting corporate events and weddings with multiple Award winning production companies. In 2017 Dane decided to establish his own brand “Dane Morrow films” that will take everything he has learned with his past experiences and push it to the next level.</p>
  <div class="btn-more">Learn More</div>
</section>

<section class="films abs" role="region" aria-label="Films">
  <span class="films-mark"></span>
  <h2 class="section-title">FILMS</h2>

  <div class="video" style="left:97px">
    <div class="video-thumb" role="img" aria-label="Couple on a stone terrace overlooking the sea" style="background:linear-gradient(180deg,#a9c8e8 0%,#d6e3ee 40%,#6f8a5e 70%,#4d5f45 100%)">
      <div class="video-controls"><div class="ctl-play"><svg width="14" height="16"><polygon points="0,0 14,8 0,16" fill="#fff"/></svg></div><div class="ctl-track"><div class="ctl-line"></div><div class="ctl-vol"></div></div></div>
    </div>
    <div class="video-title">BRENT FILM TRAILER</div>
  </div>

  <div class="video" style="left:446px">
    <div class="video-thumb" role="img" aria-label="Outdoor wedding ceremony with white flower arrangements" style="background:linear-gradient(180deg,#d8e4ee 0%,#b8c8cf 35%,#8f9a8a 65%,#e6e6e0 100%)">
      <div class="video-controls"><div class="ctl-play"><svg width="14" height="16"><polygon points="0,0 14,8 0,16" fill="#fff"/></svg></div><div class="ctl-track"><div class="ctl-line"></div><div class="ctl-vol"></div></div></div>
    </div>
    <div class="video-title">BRENT FEATURE FILM</div>
  </div>

  <div class="video" style="left:795px">
    <div class="video-thumb" role="img" aria-label="Tropical beach with rocks and a rainbow over the sea" style="background:linear-gradient(180deg,#5d8fd0 0%,#9fc1e3 35%,#4fb0b6 55%,#7a6a58 75%,#b0623f 100%)">
      <div class="video-controls"><div class="ctl-play"><svg width="14" height="16"><polygon points="0,0 14,8 0,16" fill="#fff"/></svg></div><div class="ctl-track"><div class="ctl-line"></div><div class="ctl-vol"></div></div></div>
    </div>
    <div class="video-title">JUNE AND ROB'S WEDDING</div>
  </div>
</section>

<svg class="slide-arrow" style="left:0" viewBox="0 0 36 70" aria-label="Previous">
  <polygon points="0,0 36,35 0,70" fill="#fff"/>
  <polyline points="18,27 10,35 18,43" fill="none" stroke="#555" stroke-width="2.5"/>
</svg>
<svg class="slide-arrow" style="left:1164px" viewBox="0 0 36 70" aria-label="Next">
  <polygon points="36,0 0,35 36,70" fill="#fff"/>
  <polyline points="18,27 26,35 18,43" fill="none" stroke="#555" stroke-width="2.5"/>
</svg>

<section class="blog abs">
  <h2 class="section-title">LATEST FROM <span class="accent">BLOG</span></h2>

  <article class="post" style="left:65px;top:183px;width:600px;height:392px" role="img" aria-label="Ornate historic building facade with a glass canopy entrance">
    <div style="position:absolute;inset:0;background:linear-gradient(180deg,#e8e9ea 0%,#c9c6c0 25%,#8a7558 50%,#3c3128 75%,#7a5a42 100%)"></div>
    <div class="post-caption">
      <div class="post-label">BLOG POST #1</div>
      <div class="post-text">Lorem ipsum dolor sit amet, consectetuer adipiscing elit, sed diam nonummy nibh euismod tincidunt ut laoreet dolore magna aliquam erat volutpat.</div>
    </div>
  </article>

  <article class="post" style="left:685px;top:183px;width:452px;height:185px" role="img" aria-label="Three smiling guests at an outdoor celebration">
    <div style="position:absolute;inset:0;background:linear-gradient(90deg,#e4e6e3 0%,#c7b49a 40%,#6d7563 75%,#a6b68c 100%)"></div>
    <div class="post-caption">
      <div class="post-label">BLOG POST #2</div>
      <div class="post-text">Lorem ipsum dolor sit amet, consectetuer adipiscing elit, sed diam nonummy nibh euismod tincidunt ut laoreet dolore.</div>
    </div>
  </article>

  <article class="post" style="left:685px;top:387px;width:452px;height:188px" role="img" aria-label="Couple driving a vintage convertible along a tree-lined road">
    <div style="position:absolute;inset:0;background:linear-gradient(90deg,#5f6b46 0%,#c9c0ad 40%,#3b3532 70%,#7d8a59 100%)"></div>
    <div class="post-caption">
      <div class="post-label">BLOG POST #3</div>
      <div class="post-text">Lorem ipsum dolor sit amet, consectetuer adipiscing elit, sed diam nonummy nibh euismod tincidunt ut laoreet dolore.</div>
    </div>
  </article>
</section>

<footer class="footer abs">
  <span class="footer-brand-dot"></span>
  <div class="footer-brand">DANE MORROW</div>

  <div class="footer-col" style="left:398px;width:100px">
    <div class="footer-head">QUICK LINKS</div>
    <ul class="footer-links"><li>Home</li><li>About</li><li>Films</li><li>Blog</li><li>Contact</li></ul>
  </div>

  <div class="footer-col" style="left:562px;width:215px">
    <div class="footer-head">CONTACT</div>
    <div class="contact-row">
      <svg width="16" height="18" viewBox="0 0 16 18"><circle cx="8" cy="9" r="7.5" fill="none" stroke="#fff"/><path d="M8 4a3 3 0 0 1 3 3c0 2.2-3 5.5-3 5.5S5 9.2 5 7a3 3 0 0 1 3-3z" fill="#fff"/></svg>
      <div>Dane Morrow<br>123 Example Ave<br>Los Angeles, CA 90112</div>
    </div>
    <div class="contact-row" style="margin-top:18px">
      <svg width="16" height="16" viewBox="0 0 16 16"><circle cx="8" cy="8" r="7.5" fill="none" stroke="#fff"/><path d="M5 4.5l1.5-.5 1 2-1 1c.5 1 1.5 2 2.5 2.5l1-1 2 1-.5 1.5c-3 0-6.5-3.5-6.5-6.5z" fill="#fff"/></svg>
      <div>808-555-0147</div>
    </div>
    <div class="contact-row" style="margin-top:16px">
      <svg width="16" height="16" viewBox="0 0 16 16"><circle cx="8" cy="8" r="7.5" fill="none" stroke="#fff"/><rect x="4" y="5.5" width="8" height="5.5" fill="none" stroke="#fff"/><polyline points="4,5.5 8,8.5 12,5.5" fill="none" stroke="#fff"/></svg>
      <div>dane@danemorrowfilms.example</div>
    </div>
  </div>

  <div class="footer-col" style="left:842px;width:265px">
    <div class="footer-head">NEWSLETTER</div>
    <div class="newsletter-form">
      <div class="newsletter-input">Enter Email Address</div>
      <div class="newsletter-btn">SIGN UP</div>
    </div>
  </div>
</footer>

<div class="copyright abs">COPYRIGHT © 2017 DANE MORROW. ALL RIGHTS RESERVED.</div>

</body>
</html>
```